New Web Design Project- Maplebrook Elders

Maplebrook Elders is the Capital regions premiere, non-medical, in-home care & companionship service that unites "junior-senior" caregivers with "senior-senior" care recipients so that senior-seniors can remain safe & independent in their own homes.
Our compassionate "junior-senior" caregivers are all retirees that have already enjoyed rewarding careers and/or have raised families of their own and feel the need to pay-it-forward with their care for older seniors.
Services include grocery shopping, medical or dental appointments, errands, meal preparation & cleanup, light housekeeping, bed making, laundry, hobbies, reading, transportation, entertainment, games, mobility assistance/transfers, respite care, light yard work, pet walking.

Target Market(s)

Grown children of senior-seniors between who are between 55-70, predominantly the daughters (female). End users of services (senior-seniors) are typically 80-100 years old and living in own homes

Font styles to use
Sans Serif

Colors
3277b5
ec1f27

Requirements
Must have
• supporting photos on each page. Contact us page. Promotional video (done) attached that doesn't take viewers off my site (https://vidsharehub.example/watch/Qm7rTz2KpLw).
• Also, need my downloadable brochure (attached).
• The following pages:
• Home. Services. About Us. News. Employment. Contact us. Junior-Seniors Assisting Senior-Seniors. Why non-medical in-home care. Who are junior-seniors?Financial effects of senior care. Do you need care? Does someone you love need care?
Should not have
• Any other photos or images other than what I've supplied.

```html
<!DOCTYPE html>
<html lang="en">
<head>
<meta charset="utf-8">
<title>Maplebrook Elders — Home</title>
<link href="https://fonts.googleapis.com/css2?family=Raleway:wght@400;500;600;700&display=swap" rel="stylesheet">
<style>
:root{
  --blue:#3277b5;
  --navy:#1d4f86;
  --deep:#0f3f7a;
  --red:#ec1f27;
  --maroon:#8e1c27;
  --ink:#3b3b3b;
  --muted:#7a7a7a;
  --line:#e3e6ea;
  --foot:#e8eef5;
  --row:#e4ecf4;
}
*{margin:0;padding:0;box-sizing:border-box}
html,body{width:759px;height:1200px;overflow:hidden;background:#fff}
body{font-family:"Raleway",Arial,sans-serif;color:var(--ink);position:relative}
.page{position:absolute;left:161px;top:14px;width:436px;height:1164px;border:1px solid #222;background:#fff;overflow:hidden}
.abs{position:absolute}

/* header */
.brand{left:40px;top:6px;display:flex;align-items:center;gap:4px}
.brand-mark{width:10px;height:10px;background:var(--red)}
.brand-name{font-size:7px;font-weight:700;color:var(--navy)}
.callus{right:30px;top:6px;font-size:4px;color:var(--blue)}
.tools{right:30px;top:14px;display:flex;gap:3px}
.tools span{width:5px;height:5px;border:1px solid var(--muted);border-radius:1px}
.nav{left:0;top:29px;width:436px;height:12px;background:var(--blue);display:flex;gap:0;padding-left:62px}
.nav a{font-size:4px;color:#fff;text-decoration:none;text-transform:uppercase;padding:4px 7px;letter-spacing:.2px}
.nav a.on{background:var(--navy)}

/* hero */
.hero{left:0;top:41px;width:436px;height:132px;background:linear-gradient(100deg,#a99b86 0%,#d9cbb5 35%,#f1e6da 55%,#c7b49f 80%,#8f7d6a 100%)}
.hero-title{left:90px;top:103px;width:256px;text-align:center;font-size:9px;line-height:1.25;color:var(--blue);font-weight:500;text-transform:uppercase}
.hero-arrow{top:101px;font-size:8px;color:#fff}

/* why */
.why{left:62px;top:188px;width:313px;height:115px}
.why svg{position:absolute;left:0;top:0}
.why-title{left:62px;top:198px;width:313px;text-align:center;color:#fff;font-size:17px;font-weight:400}
.why-rule{left:212px;top:224px;width:14px;height:1px;background:#fff}
.why-text{left:100px;top:230px;width:237px;text-align:center;color:#fff;font-size:4.4px;line-height:1.5}
.card{top:290px;width:78px;background:#fff;box-shadow:0 1px 4px rgba(0,0,0,.25);padding:14px 7px 8px;text-align:center;font-size:3.6px;line-height:1.55;color:var(--muted)}
.card svg{display:block;margin:0 auto 8px}
.btn{display:inline-block;background:var(--navy);color:#fff;font-size:4px;padding:3px 8px;border-radius:1px}
.btn.red{background:var(--red)}

/* research */
.research{left:62px;top:443px;width:313px;height:33px;border:1px solid var(--red);text-align:center;font-size:5.6px;line-height:1.35;color:var(--blue);padding:5px 10px}

/* banner */
.banner{left:0;top:496px;width:436px;height:59px;background:linear-gradient(90deg,#5d6f84 0%,#8a98a6 30%,#6f88a5 55%,#3d6a9a 100%)}
.banner-text{left:188px;top:506px;width:240px;text-align:center;color:#fff;font-size:7.2px;line-height:1.35}
.banner-btn{left:274px;top:532px}

/* columns */
.col-left{left:62px;top:580px;width:148px}
.col-right{left:222px;top:580px;width:153px;border-left:1px solid var(--line);padding-left:8px}
.col-title{font-size:7px;color:var(--navy);line-height:1.2;margin-bottom:7px}
.col-left ul{padding-left:9px;font-size:3.9px;line-height:1.5}
.col-left li{margin-bottom:1px}
.col-left p,.col-right p{font-size:3.9px;line-height:1.55;margin-top:5px}

/* finance */
.finance{left:62px;top:731px;width:313px;height:169px;border:1px solid var(--line)}
.fin-title{left:62px;top:738px;width:313px;text-align:center;font-size:8px;color:var(--blue)}
.fin-rule{left:62px;top:752px;width:313px;height:1px;background:var(--line)}
.fin-intro{left:72px;top:760px;width:293px;font-size:3.8px;line-height:1.4}
.cost{left:64px;top:776px;width:309px;border-collapse:collapse}
.cost th{font-weight:400;font-size:7.5px;color:var(--blue);height:15px;text-align:center}
.cost td{font-size:5.5px;color:var(--blue);height:15px;text-align:center}
.cost td:first-child,.cost th:first-child{text-align:left;padding-left:8px;width:36%}
.cost tr.shade td{background:var(--row)}
.fin-note{left:72px;top:837px;width:293px;font-size:3.8px;text-align:center}
.senior{left:64px;top:849px;width:309px;height:16px;display:flex;color:#fff;font-size:6.5px}
.senior div{display:flex;align-items:center}
.senior .c1{width:36%;background:var(--deep);padding-left:12px}
.senior .c2{width:30%;background:var(--blue);justify-content:center}
.senior .c3{width:34%;background:var(--deep);justify-content:center}
.fin-btn{left:193px;top:884px}

/* services */
.svc-title{left:0;top:920px;width:436px;text-align:center;font-size:8px;color:var(--blue)}
.svc{left:76px;top:944px;width:284px;display:flex;justify-content:space-between}
.svc-item{width:34px;height:34px;background:#d3dbe3;display:flex;flex-direction:column;align-items:center;justify-content:center;gap:2px;font-size:3px;text-align:center;color:var(--ink);line-height:1.1}
.svc-arrow{top:956px;font-size:7px;color:var(--muted)}

/* social */
.social{left:158px;top:1021px;display:flex;gap:14px}
.social span{width:14px;height:14px;border-radius:50%}
.share{left:62px;top:1044px;font-size:3.5px;color:var(--muted)}

/* footer */
.footer{left:0;top:1062px;width:436px;height:73px;background:var(--foot)}
.fcol{top:1072px;font-size:3.6px;line-height:1.55;color:var(--muted)}
.fcol h4{font-size:3.8px;font-weight:700;color:var(--navy);text-transform:uppercase;margin-bottom:3px}
.bar{left:0;top:1135px;width:436px;height:29px;background:var(--deep)}
.copy{left:62px;top:1146px;font-size:3.4px;color:#c9d6e6}
</style>
</head>
<body>
<main class="page">

  <!-- header -->
  <div class="abs brand"><span class="brand-mark"></span><span class="brand-name">Maplebrook Elders™</span></div>
  <div class="abs callus">CALL US: (555) 014-2290</div>
  <div class="abs tools"><span></span><span></span><span></span></div>
  <nav class="abs nav">
    <a class="on">Home</a><a>Services</a><a>About Us</a><a>News</a><a>Contact Us</a><a>Employment</a>
  </nav>

  <!-- hero -->
  <div class="abs hero" role="img" aria-label="Photo of two smiling senior women sharing a warm moment on a porch"></div>
  <div class="abs hero-arrow" style="left:6px">‹</div>
  <div class="abs hero-arrow" style="right:6px">›</div>
  <h1 class="abs hero-title">Maplebrook Elders™ brings comfort and companionship to people in their ripen age</h1>

  <!-- why choose us -->
  <div class="abs why" role="img" aria-label="Deep red band over a photo of a caregiver with a senior">
    <svg width="313" height="115" viewBox="0 0 313 115">
      <defs><linearGradient id="wine" x1="0" y1="0" x2="1" y2="1"><stop offset="0" stop-color="#a52a34"/><stop offset="1" stop-color="#7a1620"/></linearGradient></defs>
      <path d="M0 0H313V96Q156 125 0 96Z" fill="url(#wine)"/>
    </svg>
  </div>
  <h2 class="abs why-title">Why should you choose us ?</h2>
  <div class="abs why-rule"></div>
  <p class="abs why-text">Maplebrook Elders™ is a non-medical, in-home care and companionship service that unites retired caregivers—or Junior Seniors—with older seniors that require assistance—or Senior Seniors—to ensure that they continue to live long, happy lives in their own homes.</p>

  <div class="abs card" style="left:81px">
    <svg width="10" height="10" viewBox="0 0 10 10"><circle cx="5" cy="5" r="4.2" fill="none" stroke="#ec1f27" stroke-width="1.2"/><path d="M5 .8A4.2 4.2 0 0 1 5 9.2Z" fill="#ec1f27"/></svg>
    As a family member or friend, it's not always possible to provide the quality and quantity of care that seniors need while also attending to your own needs and responsibilities. Having someone you trust taking care of someone you love can make a big difference.
  </div>
  <div class="abs card" style="left:180px;top:283px;padding-bottom:12px">
    <svg width="10" height="11" viewBox="0 0 10 11"><circle cx="5" cy="1.6" r="1.1" fill="none" stroke="#1d4f86" stroke-width=".9"/><path d="M5 2.7V10M2.6 4.5H7.4M1 7Q2 10 5 10Q8 10 9 7" fill="none" stroke="#1d4f86" stroke-width="1"/></svg>
    Maplebrook Elders™ specializes in providing care for aging parents, family members, spouses or friends who are no longer able to live independently. Our junior-senior caregivers are just like you, who are motivated to make a difference in the lives of seniors.
  </div>
  <div class="abs card" style="left:278px">
    <svg width="10" height="10" viewBox="0 0 10 10"><path d="M5 0V10M0.7 2.5L9.3 7.5M0.7 7.5L9.3 2.5" stroke="#1e9a3c" stroke-width="2"/></svg>
    If you like the idea of being cared for by a friend who has lived a similar life, our team of junior-senior caregivers offers companionship and support, along with years of wisdom, patience and warmth.
  </div>
  <span class="abs btn" style="left:101px;top:402px">Download Brochure</span>
  <span class="abs btn" style="left:303px;top:402px">Learn more</span>

  <!-- research -->
  <p class="abs research">Research has documented a direct correlation between receiving non-medical, in-home care and the frequency of seeing doctors. Seniors who received home care reduced the frequency of doctor visits by 25%.</p>

  <!-- banner -->
  <div class="abs banner" role="img" aria-label="Photo of a caregiver helping a smiling senior man at home"></div>
  <p class="abs banner-text">Maplebrook Elders® brings comfort and companionship to the next level</p>
  <span class="abs btn banner-btn">Download Brochure</span>

  <!-- two columns -->
  <section class="abs col-left">
    <h3 class="col-title">We have solutions For Old age Problems.</h3>
    <ul>
      <li>Do you suffer from low energy, general malaise and physical problems, and/or a lack of motivation to do things?</li>
      <li>Are you having difficulty in completing daily activities in your home, such as cleaning, cooking, or laundry?</li>
      <li>Do you wish you had help getting around to keep appointments and complete errands?</li>
      <li>Could you use some help in completing your residence?</li>
    </ul>
    <p>If you answered "yes" to any or all of these questions, it may be time to investigate non-medical in-home care and companionship services from Maplebrook Elders™.</p>
  </section>
  <section class="abs col-right">
    <h3 class="col-title">How do we work ?</h3>
    <p>Receiving assistance from someone who understands how you want to live your life is the first step. After consulting with you, we pair experts from our team with caregivers who share your values, creating a comfort level and connection that lasts with your lifestyle.</p>
    <p>Junior-Seniors are made up of retirees wishing to give back to their communities. Many junior-seniors develop lasting friendships with the seniors they visit because we take the time to match you with people whose values and ideals are just like yours. Our services can be scheduled according to your needs, as little or as much as required. We think we provide a lot more than just assistance with chores and appointments — we bring people together, help each other through social interaction and share experiences that bring joy to the lives we touch.</p>
  </section>

  <!-- finance -->
  <div class="abs finance"></div>
  <h3 class="abs fin-title">Financial Details of Senior Care</h3>
  <div class="abs fin-rule"></div>
  <p class="abs fin-intro">In the most recent Hartwell Cost of Care Survey (2016), the following were the costs for the three most popular senior care options in Albany, New York:</p>
  <table class="abs cost">
    <tr><th>Albany, NY</th><th>Average Costs</th><th>Annual Cost</th></tr>
    <tr class="shade"><td>Assisted Living</td><td>$ 4,554* /month</td><td>$ 54,648</td></tr>
    <tr><td>Nursing Home(semi-private)</td><td>$ 370/day</td><td>$ 135,050</td></tr>
  </table>
  <p class="abs fin-note">Conversely, non-medical in-home care and companionship is considerably more cost efficient than that of assisted living and nursing homes.</p>
  <div class="abs senior"><div class="c1">Senior home care *</div><div class="c2">$ 24/hour</div><div class="c3">$ 37,440*</div></div>
  <span class="abs btn fin-btn">Download Brochure</span>

  <!-- services -->
  <h3 class="abs svc-title">Our Services</h3>
  <div class="abs svc-arrow" style="left:64px">‹</div>
  <div class="abs svc-arrow" style="left:366px">›</div>
  <div class="abs svc">
    <div class="svc-item"><svg width="12" height="9" viewBox="0 0 12 9"><path d="M6 2Q3 0 0 1V9Q3 8 6 9Q9 8 12 9V1Q9 0 6 2Z" fill="#222"/><path d="M6 2V9" stroke="#d3dbe3" stroke-width=".6"/></svg>Reading</div>
    <div class="svc-item"><svg width="12" height="11" viewBox="0 0 12 11"><path d="M6 0L7.5 4H12L8.3 6.5L9.7 11L6 8.2L2.3 11L3.7 6.5L0 4H4.5Z" fill="#222"/></svg>Respite care</div>
    <div class="svc-item"><svg width="12" height="10" viewBox="0 0 12 10"><path d="M0 3H12L10.5 10H1.5Z" fill="#222"/><path d="M3 3L5 0M9 3L7 0" stroke="#222"/></svg>Shopping</div>
    <div class="svc-item"><svg width="13" height="9" viewBox="0 0 13 9"><path d="M1 4L3 0.5H10L12 4V8H1Z" fill="#222"/><circle cx="3.5" cy="8" r="1.2" fill="#d3dbe3"/><circle cx="9.5" cy="8" r="1.2" fill="#d3dbe3"/></svg>Transportation to worship services</div>
    <div class="svc-item"><svg width="8" height="11" viewBox="0 0 8 11"><path d="M4 0V5" stroke="#222" stroke-width="1.2"/><path d="M1 5H7L8 11H0Z" fill="#222"/></svg><b>Errands</b>Light yard work cleaning</div>
  </div>

  <!-- social -->
  <div class="abs social" aria-label="Social links">
    <span style="background:#2f6f6a"></span><span style="background:#3a4d9a"></span><span style="background:#d4404a"></span><span style="background:#7b2d66"></span>
  </div>
  <div class="abs share">Share</div>

  <!-- footer -->
  <footer class="abs footer"></footer>
  <div class="abs fcol" style="left:62px"><h4>About Us</h4>About Us<br>Services<br>Employment<br>Contact Us</div>
  <div class="abs fcol" style="left:140px"><h4>Learn more about us</h4><span class="btn red" style="padding:4px 10px">Download Brochure</span></div>
  <div class="abs fcol" style="left:220px"><h4>Address</h4>12 Elm Hollow Road<br>Cedar Falls, NY<br>USA</div>
  <div class="abs fcol" style="left:300px"><h4>Links</h4>News<br>Contact Us<br>Privacy Policy<br>Terms and Conditions</div>
  <div class="abs bar"></div>
  <div class="abs copy">copyright © 2017 MAPLEBROOK ELDERS</div>

</main>
</body>
</html>
```